Name Card Design

Looking to create a card for my business. I am a personal stylist, my business is clothes, shoes and everything to do with looking fashion forward. I help people achieve the most polished look with cloths and grooming. I would like my card to be a reflection of my qualities which are: poise, elegance, creativity and fairness.
Things I like a simple yet expensive looking, sometimes less simple but highly creative and different catches my eye. For instance I saw a card with lace trimming at the bottom, it made me think about the business that person was in. I don't like childish designs with butterflies, trees, flowers, etc.
Here is my site www.Marta-Vosel.example for your perusal

On the card it should have the following info
Marta Vosel
personal stylist
www.Marta-Vosel.example
(+65) 482-30857
Facebook page: Ringthelook

Back of the card:
Wardrobe weeding
Personal shopping
Style consultation

Target Market(s)

mostly working women

Industry/Entity Type

Fashion

Font styles to use
Serif
Sans Serif

Requirements
Should not have
• butterflies, flowers, feathers, etc

```html
<!DOCTYPE html>
<html lang="en">
<head>
<meta charset="utf-8">
<title>Marta Vosel – Personal Stylist</title>
<link rel="stylesheet" href="https://fonts.googleapis.com/css2?family=Bodoni+Moda:opsz,wght@6..96,700&family=Source+Sans+3:wght@400&display=swap">
<style>
  :root {
    --backdrop: #e8e5e1;
    --card-deep: #0c0b0b;
    --card-mid: #262423;
    --ink: #f4f2ef;
    --icon: #d9d6d2;
  }
  html, body {
    margin: 0;
    padding: 0;
    width: 1200px;
    height: 767px;
    overflow: hidden;
    background: var(--backdrop);
  }
  .stage {
    position: relative;
    width: 1200px;
    height: 767px;
  }
  .card {
    position: absolute;
    left: 85px;
    top: 85px;
    width: 1030px;
    height: 587px;
    overflow: hidden;
    box-shadow: 0 2px 6px rgba(0,0,0,.25);
  }
  .card-surface {
    position: absolute;
    inset: 0;
    background: radial-gradient(ellipse at 50% 40%, var(--card-mid) 0%, #181716 55%, var(--card-deep) 100%);
  }
  .name {
    position: absolute;
    left: 0;
    right: 0;
    top: 92px;
    margin: 0;
    text-align: center;
    font-family: "Bodoni Moda", "Times New Roman", serif;
    font-weight: 700;
    font-size: 112px;
    line-height: 1;
    color: var(--ink);
    letter-spacing: -1px;
    transform: scaleX(0.86);
  }
  .role {
    position: absolute;
    left: 0;
    right: 0;
    top: 232px;
    margin: 0;
    text-align: center;
    font-family: "Bodoni Moda", "Times New Roman", serif;
    font-weight: 700;
    font-size: 44px;
    line-height: 1;
    color: var(--ink);
    transform: scaleX(0.78);
  }
  .contact-list {
    position: absolute;
    left: 30px;
    top: 334px;
    margin: 0;
    padding: 0;
    list-style: none;
  }
  .contact-list li,
  .service {
    display: flex;
    align-items: center;
    font-family: "Source Sans 3", "Myriad Pro", sans-serif;
    color: var(--ink);
  }
  .contact-list li {
    height: 52.5px;
    font-size: 27px;
  }
  .contact-list svg {
    width: 22px;
    height: 22px;
    margin-right: 20px;
  }
  .social-dot {
    width: 16px;
    height: 16px;
    margin: 0 22px 0 3px;
    border: 2px solid var(--icon);
    border-radius: 50%;
    box-sizing: border-box;
  }
  .services {
    position: absolute;
    left: 32px;
    top: 506px;
    display: flex;
    align-items: center;
  }
  .service {
    font-size: 31px;
    margin-right: 22px;
  }
  .service svg {
    width: 28px;
    height: 26px;
    margin-right: 10px;
  }
  .service.style-consult svg { width: 40px; }
  .icon-line {
    fill: none;
    stroke: var(--icon);
    stroke-width: 1.6;
    stroke-linecap: round;
    stroke-linejoin: round;
  }
</style>
</head>
<body>
<main class="stage">
  <section class="card">
    <div class="card-surface" role="img" aria-label="Black leather texture background"></div>

    <h1 class="name">Marta Vosel</h1>
    <p class="role">Personal Stylist</p>

    <ul class="contact-list">
      <li>
        <svg viewBox="0 0 22 22" aria-hidden="true">
          <circle class="icon-line" cx="11" cy="11" r="9"/>
          <path class="icon-line" d="M8 6c-1 2 0 6 3 9 1 1 2 1 3 0l-1-2-1.5 .5c-1-1-2-3-2-4.5l1.5-.8L10 6z"/>
        </svg>
        (+65) 482-30857
      </li>
      <li>
        <svg viewBox="0 0 22 22" aria-hidden="true">
          <circle class="icon-line" cx="11" cy="11" r="9"/>
          <ellipse class="icon-line" cx="11" cy="11" rx="4" ry="9"/>
          <path class="icon-line" d="M2 11h18M4 6h14M4 16h14"/>
        </svg>
        www.Marta-Vosel.example
      </li>
      <li>
        <span class="social-dot" aria-hidden="true"></span>
        Ringthelook
      </li>
    </ul>

    <div class="services">
      <span class="service wardrobe">
        <svg viewBox="0 0 28 26" aria-hidden="true">
          <path class="icon-line" d="M11 6a3 3 0 1 1 5 2.2L14 10M14 10L4 22h20z"/>
        </svg>
        Wardrobe Weeding
      </span>
      <span class="service shopping">
        <svg viewBox="0 0 28 26" aria-hidden="true">
          <path class="icon-line" d="M2 5h4l3 12h14l2-9H8"/>
          <circle class="icon-line" cx="11" cy="21" r="1.8"/>
          <circle class="icon-line" cx="21" cy="21" r="1.8"/>
        </svg>
        Personal Shopping
      </span>
      <span class="service style-consult">
        <svg viewBox="0 0 40 26" aria-hidden="true">
          <path class="icon-line" d="M3 11c0-5 6-8 12-8s12 3 12 8-6 8-12 8l-6 4 1-5c-4-1-7-4-7-7z"/>
          <path class="icon-line" d="M20 16c2 3 6 4 10 4l5 3-1-4c2-1 4-3 4-6 0-3-3-5-7-6"/>
          <circle cx="27" cy="14" r="1.2" fill="var(--icon)"/>
          <circle cx="31" cy="14" r="1.2" fill="var(--icon)"/>
          <circle cx="35" cy="14" r="1.2" fill="var(--icon)"/>
        </svg>
        Style consultation
      </span>
    </div>
  </section>
</main>
</body>
</html>
```